Business card and stationary package

Travel management company looking for designs for single sided business cards, letterhead and envelope. Looking for contemporary designs using our existing logo. Design should clean, not trendy, no gradation of colors and no graphic other than the icon from the logo. Nothing complicated or difficult to read. Should be a crisp design using blue, gray and black colors only.
Letterhead should include a Word template and PDF template.
Business cards are one sided as the reverse will be dynamic images in our company portfolio of images.
We will use the same designer periodically for design projects using the same style guide for upcoming projects as well. Prefer working with designer that will assist with website, brochures and other marketing materials.

Logo Colors and Font:
Blue: 2189c6 Color Hex
Gray: 666666 Color Hex 60% Black
Black: 100% Black
Font: Century Gothic

Target Market(s)

business-to-business

Industry/Entity Type

Travel Industry

Contact Information for Business Card

Sample information for business cards will be:

Daniel Fenwick
Managing Partner

Harborline Journey Services, Inc.
274 Alder Lane, Suite 3621
Dunmore, VT 05231

207-555-0148 Direct Dial
207-555-0193 Fax

daniel@harborlinejourney.net
www.harborlinejourney.net

Font styles to use
Sans Serif

Requirements
Must have
• Clean, crisp design, easy to ready, memorable.
Nice to have
• We tend to like dynamic designs that are simple, not trendy, contemporary and easy to read.
Should not have
• no gradation of colors and no graphic other than the icon from the logo, no background images
• **Note that the background should only be white. No black/gary backgrounds or graded colors**

```html
<!DOCTYPE html>
<html lang="en">
<head>
<meta charset="utf-8">
<title>Harborline Journey Services – Business Card</title>
<link href="https://fonts.googleapis.com/css2?family=Open+Sans:wght@400;700&display=swap" rel="stylesheet">
<style>
  :root {
    --brand-blue: #2189c6;
    --brand-gray: #666666;
    --ink: #000000;
    --card-white: #ffffff;
    --page-bg: #eeeeee;
    --rule-gray: #8a8a8a;
  }
  * { box-sizing: border-box; margin: 0; padding: 0; }
  html, body {
    width: 1200px;
    height: 1022px;
    overflow: hidden;
    background: var(--page-bg);
    font-family: "Open Sans", Arial, sans-serif;
  }
  .business-card {
    position: absolute;
    left: 100px;
    top: 225px;
    width: 1000px;
    height: 572px;
    background: var(--card-white);
    border-radius: 22px;
    box-shadow: 0 2px 10px rgba(0,0,0,0.12);
  }
  .brand-lockup {
    position: absolute;
    left: 250px;
    top: 240px;
    display: flex;
    align-items: center;
    gap: 20px;
  }
  .brand-dot {
    width: 64px;
    height: 64px;
    border-radius: 50%;
    background: var(--brand-blue);
  }
  .brand-name {
    font-size: 34px;
    font-weight: 400;
    letter-spacing: 3px;
    color: var(--brand-gray);
    text-transform: uppercase;
  }
  .blue-rule {
    position: absolute;
    left: 0;
    right: 0;
    top: 352px;
    height: 2px;
    background: var(--brand-blue);
  }
  .person-block {
    position: absolute;
    left: 150px;
    top: 378px;
    width: 330px;
    text-align: right;
  }
  .person-name {
    font-size: 30px;
    font-weight: 700;
    color: var(--brand-blue);
    text-transform: uppercase;
    line-height: 1.15;
  }
  .person-title {
    font-size: 17px;
    color: var(--brand-gray);
    text-transform: uppercase;
    letter-spacing: 1px;
    margin-bottom: 6px;
  }
  .address-line {
    font-size: 19px;
    color: var(--brand-gray);
    line-height: 1.35;
  }
  .column-divider {
    position: absolute;
    left: 502px;
    top: 378px;
    width: 2px;
    height: 150px;
    background: var(--rule-gray);
  }
  .contact-list {
    position: absolute;
    left: 526px;
    top: 380px;
    list-style: none;
  }
  .contact-item {
    display: flex;
    align-items: center;
    gap: 10px;
    font-size: 19px;
    color: var(--brand-gray);
    line-height: 1.5;
  }
  .contact-icon {
    width: 16px;
    height: 16px;
    flex: none;
  }
  .contact-icon * { fill: none; stroke: var(--brand-blue); stroke-width: 2; }
  .contact-icon .solid { fill: var(--brand-blue); stroke: none; }
</style>
</head>
<body>
  <div class="business-card">
    <div class="brand-lockup">
      <div class="brand-dot"></div>
      <div class="brand-name">Harborline Journey Services</div>
    </div>

    <div class="blue-rule"></div>

    <div class="person-block">
      <div class="person-name">Daniel Fenwick</div>
      <div class="person-title">Managing Partner</div>
      <div class="address-line">274 Alder Lane, Suite 3621</div>
      <div class="address-line">Dunmore, VT 05231</div>
    </div>

    <div class="column-divider"></div>

    <ul class="contact-list">
      <li class="contact-item">
        <svg class="contact-icon" viewBox="0 0 16 16"><path class="solid" d="M3 1l3 3-1.5 2c1 2 3 4 5 5l2-1.5 3 3-2 2C7 14 2 9 1 3z"/></svg>
        207-555-0148 Direct
      </li>
      <li class="contact-item">
        <svg class="contact-icon" viewBox="0 0 16 16"><rect class="solid" x="4" y="1" width="8" height="5"/><rect class="solid" x="1" y="7" width="14" height="5" rx="1"/><rect class="solid" x="4" y="12" width="8" height="3"/></svg>
        207-555-0193
      </li>
      <li class="contact-item">
        <svg class="contact-icon" viewBox="0 0 16 16"><rect x="1.5" y="3.5" width="13" height="9"/><path d="M1.5 3.5l6.5 5 6.5-5"/></svg>
        daniel@harborlinejourney.net
      </li>
      <li class="contact-item">
        <svg class="contact-icon" viewBox="0 0 16 16"><circle cx="8" cy="8" r="6.5"/><ellipse cx="8" cy="8" rx="3" ry="6.5"/><path d="M1.5 8h13"/></svg>
        www.harborlinejourney.net
      </li>
    </ul>
  </div>
</body>
</html>
```